Business Card - I already have a Logo

I have a logo, I just want a business card designed that uses it. I would like to see designs that are very clean, have a sense of health and wellbeing, up-market clientele.

Target Market(s)

People interested in health and well-being, people with money! Ages 25-70

Industry/Entity Type

Massage Therapy

Contact Information for Business Card

Tomas Brevin
Integrative Bodyworker

KaHuna, Remedial, Pregnancy & Maya Abdominal Massage, Body Based Psychology. Health fund rebates available
0437615290
info@wenmorestill.com.au

Colors
86cfc6
33b8a4
00a990
85cae6
cee9f5
33a6d7
85acd3
3276b5
0355a3

Requirements
Must have
• Clean, simple, elegant design, using my existing logo

```html
<!DOCTYPE html>
<html lang="en">
<head>
<meta charset="utf-8">
<title>Wenmore Still &amp; Massage — Business Card</title>
<link href="https://fonts.googleapis.com/css2?family=Cabin:wght@400;600&family=Crimson+Text:ital,wght@1,400;1,700&display=swap" rel="stylesheet">
<style>
  :root {
    --backdrop: #333132;
    --card-white: #ffffff;
    --brand-blue: #0096d6;
    --ink-grey: #4a4a4a;
    --sand-light: #e4d6c4;
    --sand-mid: #c9a98a;
    --sand-warm: #c98a3e;
    --rock-dark: #5a4c44;
  }
  * { margin: 0; padding: 0; box-sizing: border-box; }
  html, body {
    width: 962px; height: 1200px; overflow: hidden;
    background: var(--backdrop);
  }
  .stage { position: relative; width: 962px; height: 1200px; }

  .card {
    position: absolute; left: 80px; width: 803px; height: 485px;
    overflow: hidden;
  }
  .card--front { top: 97px; }
  .card--back { top: 618px; background: var(--card-white); }

  .front-photo {
    position: absolute; inset: 0;
    background:
      radial-gradient(ellipse at 78% 85%, var(--rock-dark) 0%, rgba(90,76,68,0) 40%),
      radial-gradient(ellipse at 15% 45%, var(--sand-warm) 0%, rgba(201,138,62,0) 45%),
      linear-gradient(120deg, var(--sand-mid) 0%, var(--sand-light) 45%, #d8c6b2 70%, #8a7566 100%);
  }
  .brand {
    position: absolute; left: 0; right: 0; top: 130px;
    text-align: center; color: var(--card-white);
    font-family: 'Cabin', sans-serif; font-weight: 600;
  }
  .brand__dot {
    display: block; width: 92px; height: 92px; margin: 0 auto 38px;
    border-radius: 50%; background: var(--card-white);
  }
  .brand__name { display: block; font-size: 48px; line-height: 1; letter-spacing: -0.5px; }
  .brand__sub { display: block; font-size: 22px; line-height: 1; margin-top: 14px; letter-spacing: 12px; padding-left: 12px; }

  .person {
    position: absolute; left: 422px; top: 108px;
    font-family: 'Crimson Text', serif; font-style: italic;
  }
  .person__name { font-size: 51px; font-weight: 700; color: var(--brand-blue); line-height: 1; }
  .person__role { font-size: 24px; font-weight: 400; color: var(--ink-grey); margin-top: 2px; letter-spacing: 0.6px; }

  .contact {
    position: absolute; left: 422px; top: 260px;
    list-style: none;
    font-family: 'Crimson Text', serif; font-style: italic;
    font-size: 21px; line-height: 32.5px; color: var(--ink-grey); letter-spacing: 1.2px;
  }

  .services {
    position: absolute; left: 0; bottom: 0; width: 100%; height: 88px;
    background: var(--brand-blue); color: var(--card-white);
    font-family: 'Cabin', sans-serif; font-size: 22px; line-height: 29px;
    text-align: center; padding-top: 14px;
  }
  .services strong { font-weight: 600; }
</style>
</head>
<body>
<main class="stage">
  <section class="card card--front">
    <div class="front-photo" role="img" aria-label="Photograph of weathered coastal sandstone cliffs in ochre and cream tones"></div>
    <div class="brand">
      <span class="brand__dot"></span>
      <span class="brand__name">Wenmore Still</span>
      <span class="brand__sub">&amp; MASSAGE</span>
    </div>
  </section>

  <section class="card card--back">
    <div class="person">
      <h1 class="person__name">Tomas Brevin</h1>
      <p class="person__role">Integrative Bodyworker</p>
    </div>
    <ul class="contact">
      <li>0437 615 290</li>
      <li>info@wenmorestill.com.au</li>
      <li>www.wenmorestill.com.au</li>
    </ul>
    <p class="services">KaHuna, Remedial, Pregnancy &amp; Maya Abdominal Massage,<br>Body Based Psychology. <strong>Health fund rebates available</strong></p>
  </section>
</main>
</body>
</html>
```